Re-branding for Structural Engineering firm

We need new business cards as part of our current re-branding. We have a new logo (attached), so the card design should incorporate this color scheme. We are a structural engineering firm providing structural building design and seismic consulting services. The final design should communicate professionalism and stability, with a modern look and feel.

```html
<!DOCTYPE html>
<html lang="en">
<head>
<meta charset="utf-8">
<title>RMK Structural Engineering – Business Card</title>
<link href="https://fonts.googleapis.com/css2?family=Open+Sans:wght@400;700&display=swap" rel="stylesheet">
<style>
  :root {
    --stage-grey: #808184;
    --brand-blue: #1b75bc;
    --brand-grey: #808184;
    --card-white: #ffffff;
    --text-grey: #6d6e71;
  }
  * { margin: 0; padding: 0; box-sizing: border-box; }
  html, body { width: 1200px; height: 427px; overflow: hidden; }
  body {
    background: var(--stage-grey);
    font-family: "Open Sans", Arial, sans-serif;
    position: relative;
  }
  .card {
    position: absolute;
    background: var(--card-white);
    overflow: hidden;
  }
  .card-front { left: 102px; top: 94px; width: 479px; height: 268px; }
  .card-back  { left: 626px; top: 96px; width: 477px; height: 266px; }
  .card-shapes { position: absolute; inset: 0; width: 100%; height: 100%; }
  .shape-blue { fill: var(--brand-blue); }
  .shape-grey { fill: var(--brand-grey); }

  .holder-name {
    position: absolute; left: 35px; top: 24px;
    font-size: 24px; font-weight: 700; color: var(--brand-blue);
    letter-spacing: 0.2px;
  }
  .holder-title {
    position: absolute; left: 170px; top: 56px;
    font-size: 13.5px; color: var(--text-grey);
  }
  .contact-icon {
    position: absolute; width: 28px; height: 28px;
  }
  .contact-icon circle { fill: var(--brand-grey); }
  .contact-icon .glyph { fill: var(--card-white); }
  .contact-icon .glyph-line { fill: none; stroke: var(--card-white); stroke-width: 1.6; }
  .contact-text {
    position: absolute; font-size: 13.5px; line-height: 17px; color: var(--text-grey);
    transform: translateY(-50%);
  }
  .icon-pin   { left: 95px;  top: 100px; }
  .icon-phone { left: 124px; top: 144px; }
  .icon-mobile{ left: 153px; top: 180px; }
  .icon-mail  { left: 181px; top: 217px; }
  .text-address { left: 137px; top: 118px; }
  .text-phone   { left: 174px; top: 156px; }
  .text-mobile  { left: 202px; top: 194px; }
  .text-mail    { left: 220px; top: 231px; }

  .brand-block {
    position: absolute; left: 186px; top: 76px; width: 106px;
    display: flex; flex-direction: column; align-items: center;
  }
  .brand-square {
    width: 66px; height: 66px; background: var(--brand-blue);
    margin-bottom: 10px;
  }
  .brand-name {
    font-size: 15px; font-weight: 700; color: var(--brand-blue);
    text-align: center; line-height: 16px; text-transform: uppercase;
  }
</style>
</head>
<body>

<section class="card card-front">
  <svg class="card-shapes" viewBox="0 0 598 334" preserveAspectRatio="none">
    <polygon class="shape-blue" points="407,0 598,0 598,55 464,55"/>
    <polygon class="shape-grey" points="477,68 598,68 598,126 532,126"/>
    <polygon class="shape-blue" points="546,140 598,140 598,192"/>
    <polygon class="shape-blue" points="0,138 55,193 0,193"/>
    <polygon class="shape-grey" points="0,207 66,207 122,263 0,263"/>
    <polygon class="shape-blue" points="0,277 137,277 192,334 0,334"/>
  </svg>

  <h1 class="holder-name">DANA MERROW, S.E</h1>
  <p class="holder-title">PRINCIPAL</p>

  <svg class="contact-icon icon-pin" viewBox="0 0 28 28">
    <circle cx="14" cy="14" r="14"/>
    <path class="glyph" d="M14 6.5a5 5 0 0 0-5 5c0 3.8 5 9.5 5 9.5s5-5.7 5-9.5a5 5 0 0 0-5-5zm0 6.8a1.8 1.8 0 1 1 0-3.6 1.8 1.8 0 0 1 0 3.6z"/>
  </svg>
  <p class="contact-text text-address">4170 Harbor Ridge Rd., Ste 210<br>Lakeview, CA 92044</p>

  <svg class="contact-icon icon-phone" viewBox="0 0 28 28">
    <circle cx="14" cy="14" r="14"/>
    <path class="glyph" d="M10.2 7.5l2 3.2-1.4 1.4c.7 1.8 2 3.3 3.8 4.3l1.4-1.4 3.2 2-1 2.6c-4.8-.2-9.5-4.9-9.6-9.8z"/>
  </svg>
  <p class="contact-text text-phone">555.204.1183</p>

  <svg class="contact-icon icon-mobile" viewBox="0 0 28 28">
    <circle cx="14" cy="14" r="14"/>
    <rect class="glyph-line" x="9.8" y="6.8" width="8.4" height="14.4" rx="1.5"/>
    <circle class="glyph" cx="14" cy="18.6" r="0.9" style="fill:#fff"/>
  </svg>
  <p class="contact-text text-mobile">555.730.4926</p>

  <svg class="contact-icon icon-mail" viewBox="0 0 28 28">
    <circle cx="14" cy="14" r="14"/>
    <rect class="glyph-line" x="7.5" y="9.5" width="13" height="9" rx="1"/>
    <polyline class="glyph-line" points="7.8,10 14,14.8 20.2,10"/>
  </svg>
  <p class="contact-text text-mail">dana@rmkse.com</p>
</section>

<section class="card card-back">
  <svg class="card-shapes" viewBox="0 0 596 333" preserveAspectRatio="none">
    <polygon class="shape-blue" points="0,0 190,0 135,55 0,55"/>
    <polygon class="shape-grey" points="0,72 117,72 62,130 0,130"/>
    <polygon class="shape-blue" points="0,144 48,144 0,192"/>
    <polygon class="shape-blue" points="596,137 596,190 542,190"/>
    <polygon class="shape-grey" points="530,205 596,205 596,261 475,261"/>
    <polygon class="shape-blue" points="460,277 596,277 596,333 404,333"/>
  </svg>

  <div class="brand-block">
    <div class="brand-square"></div>
    <p class="brand-name">RMK<br>Structural<br>Engineering</p>
  </div>
</section>

</body>
</html>
```